Data Analytics Irish company needs Stationery Design

We need a stationery design for our data analytics company based in Dublin called 'Numbryx': we develop innovative web-based corporate applications exploiting advanced Machine Learning and Data Mining techniques.
Like the animal that inspired our company name, the final design should communicate intelligence and passion; on the other hand, we want to keep the highest professional appeal.
We love our current logo and we have tried out several color variations: we prefer solutions (see the logo attached) with white design and dark backgrounds, but we will also be glad to see some designs that follow the colors of the palette of the attached web screenshot.

```html
<!DOCTYPE html>
<html lang="en">
<head>
<meta charset="utf-8">
<title>Numbryx Stationery</title>
<link href="https://fonts.googleapis.com/css2?family=Exo+2:wght@400;600&display=swap" rel="stylesheet">
<style>
  :root {
    --bg: #e4e4e4;
    --paper: #ffffff;
    --brand: #1a5fb4;
    --brand-deep: #0d4c9c;
    --brand-light: #2f86d6;
    --wash: #e3eef7;
    --ink: #4a4f57;
    --shadow: 0 6px 18px rgba(0,0,0,0.12);
  }
  * { box-sizing: border-box; margin: 0; padding: 0; }
  html, body { width: 1200px; height: 900px; overflow: hidden; }
  body {
    background: var(--bg);
    font-family: "Exo 2", sans-serif;
    position: relative;
  }
  .piece { position: absolute; background: var(--paper); box-shadow: var(--shadow); overflow: hidden; }
  .wordmark {
    font-family: "Exo 2", sans-serif;
    font-weight: 600;
    color: var(--brand);
    display: flex;
    align-items: center;
    gap: 8px;
    line-height: 1;
  }
  .wordmark .dot { border-radius: 50%; background: currentColor; flex: none; }

  /* envelope back */
  .envelope-back { left: 60px; top: 60px; width: 520px; height: 250px; }
  .envelope-back svg { position: absolute; left: 0; top: 0; }

  /* envelope front */
  .envelope-front { left: 60px; top: 340px; width: 520px; height: 250px; }
  .envelope-front .sender { position: absolute; left: 34px; top: 34px; }
  .envelope-front .wordmark { font-size: 24px; }
  .envelope-front .wordmark .dot { width: 14px; height: 14px; }
  .sender .address { margin-top: 8px; font-size: 8px; color: var(--ink); line-height: 1.35; }

  /* long sheet with centred mark */
  .sheet { left: 620px; top: 300px; width: 520px; height: 290px; }
  .sheet .faint-disc { position: absolute; left: -80px; top: 10px; width: 260px; height: 260px; border-radius: 50%; background: var(--wash); }
  .sheet .wordmark { position: absolute; left: 250px; top: 110px; font-size: 28px; }
  .sheet .wordmark .dot { width: 16px; height: 16px; }

  /* business card back */
  .card-back { left: 640px; top: 60px; width: 340px; height: 195px; }
  .card-back .disc { position: absolute; left: -70px; top: -25px; width: 240px; height: 245px; border-radius: 50%; background: var(--brand); }
  .card-back .contact { position: absolute; right: 26px; top: 78px; text-align: right; font-size: 12px; color: var(--ink); line-height: 1.5; }

  /* business card front */
  .card-front {
    left: 60px; top: 630px; width: 360px; height: 205px;
    background: linear-gradient(135deg, var(--brand-deep), var(--brand-light) 60%, var(--brand));
    display: flex; align-items: center; justify-content: center;
  }
  .card-front .wordmark { color: #ffffff; font-size: 42px; gap: 12px; }
  .card-front .wordmark .dot { width: 22px; height: 22px; }

  /* standalone mark */
  .standalone { position: absolute; left: 900px; top: 770px; }
  .standalone .wordmark { font-size: 46px; gap: 12px; }
  .standalone .wordmark .dot { width: 24px; height: 24px; }
</style>
</head>
<body>
  <div class="piece envelope-back">
    <svg width="520" height="250" viewBox="0 0 520 250" aria-hidden="true">
      <defs>
        <linearGradient id="flap" x1="0" y1="0" x2="1" y2="0">
          <stop offset="0" stop-color="#0d4c9c"/>
          <stop offset="0.5" stop-color="#2f86d6"/>
          <stop offset="1" stop-color="#0d4c9c"/>
        </linearGradient>
      </defs>
      <polygon points="0,0 520,0 520,14 0,44" fill="url(#flap)"/>
    </svg>
  </div>

  <div class="piece envelope-front">
    <div class="sender">
      <div class="wordmark"><span class="dot"></span>numbryx</div>
      <p class="address">00 Street, 00th Floor<br>City, City 00000<br>Phone: 000 000 000<br>www.numbryx.ie</p>
    </div>
  </div>

  <div class="piece sheet">
    <div class="faint-disc"></div>
    <div class="wordmark"><span class="dot"></span>numbryx</div>
  </div>

  <div class="piece card-back">
    <div class="disc"></div>
    <div class="contact">000 000 000<br>www.numbryx.ie</div>
  </div>

  <div class="piece card-front">
    <div class="wordmark"><span class="dot"></span>numbryx</div>
  </div>

  <div class="standalone">
    <div class="wordmark"><span class="dot"></span>numbryx</div>
  </div>
</body>
</html>
```